New Business Card

Would like a shiny card with Metallic logo raised on th front. Address 418 Kestwick Lane, Toronto Ontario M4T2B8, phone 416 555 0382, email kmvc@lorentel.ca and web www.kmvc.ca on the back in right and left lower corners balanced. Top of back should say Personalized Care for Pet's and their People centered. Leaving space on the back to write. Horizontal placement

```html
<!DOCTYPE html>
<html lang="en">
<head>
<meta charset="utf-8">
<title>Kestwick Mews Animal Clinic — Business Card</title>
<link href="https://fonts.googleapis.com/css2?family=Open+Sans:wght@400&display=swap" rel="stylesheet">
<style>
  :root {
    --backdrop: #1b1c1e;
    --card-top: #2a2a2c;
    --card-bottom: #1a1a1b;
    --card-edge: #3a3a3d;
    --emboss: #4a4a4e;
    --emboss-light: #5b5b60;
    --ink: #f2f2f2;
  }
  * { margin: 0; padding: 0; box-sizing: border-box; }
  html, body {
    width: 1200px;
    height: 900px;
    overflow: hidden;
    background: var(--backdrop);
    font-family: "Open Sans", Arial, sans-serif;
  }
  .canvas {
    width: 1200px;
    height: 900px;
    display: flex;
    flex-direction: column;
    align-items: center;
    justify-content: center;
    gap: 40px;
  }
  .card {
    position: relative;
    width: 660px;
    height: 377px;
    background: linear-gradient(160deg, var(--card-top), var(--card-bottom));
    border: 1px solid var(--card-edge);
    box-shadow: 0 14px 30px rgba(0, 0, 0, 0.55);
  }

  /* Front */
  .card-front {
    display: flex;
    flex-direction: column;
    align-items: center;
    justify-content: center;
    gap: 22px;
  }
  .brand-mark {
    width: 64px;
    height: 64px;
    border-radius: 50%;
    background: var(--emboss);
    box-shadow: inset 1px 1px 2px var(--emboss-light), inset -1px -1px 2px #1e1e20;
  }
  .brand-name {
    font-weight: 400;
    font-size: 30px;
    letter-spacing: 4px;
    text-transform: uppercase;
    color: var(--emboss);
    text-align: center;
  }

  /* Back */
  .tagline {
    position: absolute;
    top: 44px;
    left: 0;
    right: 0;
    text-align: center;
    font-size: 20px;
    color: var(--ink);
  }
  .contact {
    position: absolute;
    left: 44px;
    bottom: 40px;
    color: var(--ink);
    font-size: 17px;
    line-height: 1.35;
  }
  .address { margin-bottom: 8px; padding-left: 10px; }
  .contact-list { list-style: none; }
  .contact-list li {
    display: flex;
    align-items: center;
    gap: 12px;
  }
  .contact-list svg {
    width: 16px;
    height: 16px;
    flex: none;
    fill: none;
    stroke: var(--ink);
    stroke-width: 1.6;
    stroke-linecap: round;
    stroke-linejoin: round;
  }
</style>
</head>
<body>
<main class="canvas">
  <section class="card card-front" aria-label="Card front">
    <div class="brand-mark"></div>
    <div class="brand-name">Kestwick Mews Animal Clinic</div>
  </section>

  <section class="card card-back" aria-label="Card back">
    <p class="tagline">Personalized Care for Pet's and their People</p>
    <div class="contact">
      <p class="address">418 Kestwick Lane<br>Toronto Ontario M4T2B8</p>
      <ul class="contact-list">
        <li>
          <svg viewBox="0 0 16 16" aria-hidden="true"><path d="M4 2l2 3-1.5 1.5a8 8 0 0 0 5 5L11 10l3 2-1.5 2.5A10 10 0 0 1 1.5 3.5z"/></svg>
          <span>416 555 0382</span>
        </li>
        <li>
          <svg viewBox="0 0 16 16" aria-hidden="true"><rect x="1.5" y="3.5" width="13" height="9"/><path d="M1.5 3.5L8 9l6.5-5.5"/></svg>
          <span>kmvc@lorentel.ca</span>
        </li>
        <li>
          <svg viewBox="0 0 16 16" aria-hidden="true"><circle cx="8" cy="8" r="6.5"/><path d="M1.5 8h13M8 1.5c-3 3.5-3 9.5 0 13M8 1.5c3 3.5 3 9.5 0 13"/></svg>
          <span>www.kmvc.ca</span>
        </li>
      </ul>
    </div>
  </section>
</main>
</body>
</html>
```